An A2 office artwork piece with quote overlay

I would like a piece of A2 office artwork, inspired by two things important to me and my business, overlaid with a quote. I have attached some photos and I have the quote I would like. My office is dark, minimalistic and modern in design (photo attached). I would like the artwork to contain some element of colour, but it should not be bright, the quote should be the main element with the photo and further design elements creating a subtle background.

The art will go on the wall behind my office chair and will appear in most of my online business video content, therefore I would like it to be inspiring.

The quote to be used:

"It is not because things are difficult that we do not dare; it is because we do not dare that they are difficult." - Talvio

The property in the attached photograph is one we purchased recently and is an important milestone in my business.

I would also like an aviation reference to feature in the background as this was my career before I started my property business and I'm currently training to be a flying instructor. I have attached some aircraft photos which I have taken and I've attached some other items for inspiration. I am open to how the aviation reference is blended in.

Target Market(s)

This isn't a sales piece, it just needs to be intriguing.

Industry/Entity Type

Real estate

Font styles to use
Serif
Sans Serif
Script

Requirements
Must have
• Must have the building in the attached photograph and the quote.
Nice to have
• An aviation reference if this can be blended within the background.
Should not have
• Too many bright colours

```html
<!DOCTYPE html>
<html lang="en">
<head>
<meta charset="utf-8">
<title>Office Artwork – Quote Poster</title>
<link rel="stylesheet" href="https://fonts.googleapis.com/css2?family=Josefin+Sans:wght@600&family=Oswald:wght@700&display=swap">
<style>
  :root {
    --backdrop: #1f1f20;
    --poster-base: #2a2b2d;
    --poster-deep: #1d1e20;
    --frame-black: #101012;
    --panel-top: #2b2c2f;
    --panel-bottom: #202123;
    --facet-light: #6a6b6e;
    --facet-mid: #3a3b3e;
    --facet-dark: #161618;
    --gold: #a98458;
    --instrument-tone: #4a4b48;
    --brick-tone: #5a3a32;
    --line-drawing: rgba(200, 200, 205, 0.18);
  }
  html, body {
    margin: 0;
    width: 1200px;
    height: 704px;
    overflow: hidden;
    background: var(--backdrop);
  }
  .poster {
    position: absolute;
    left: 366px;
    top: 22px;
    width: 467px;
    height: 660px;
    background: linear-gradient(160deg, var(--poster-base), var(--poster-deep));
    overflow: hidden;
  }
  .poster > * { position: absolute; }
  .facets { left: 0; top: 0; width: 467px; height: 660px; }
  .instrument-panel {
    left: 236px; top: 5px; width: 231px; height: 130px;
    background: radial-gradient(ellipse at 60% 40%, var(--instrument-tone), transparent 75%);
    opacity: 0.8;
  }
  .back-frame {
    left: 82px; top: 81px; width: 304px; height: 499px;
    background: var(--frame-black);
  }
  .quote-panel {
    left: 110px; top: 109px; width: 248px; height: 442px;
    background: linear-gradient(160deg, var(--panel-top), var(--panel-bottom));
  }
  .building-photo {
    left: 33px; top: 413px; width: 302px; height: 218px;
    background: linear-gradient(to bottom, transparent 0%, rgba(90,58,50,0.55) 35%, rgba(70,50,45,0.7) 70%, rgba(35,35,37,0.9) 100%);
  }
  .aircraft-drawing { background: var(--line-drawing); border-radius: 3px; }
  .aircraft-top { left: 289px; top: 131px; width: 126px; height: 36px; }
  .aircraft-left { left: 10px; top: 177px; width: 99px; height: 54px; }
  .aircraft-bottom { left: 335px; top: 454px; width: 79px; height: 97px; }
  .quote-mark {
    font-family: "Oswald", sans-serif;
    font-weight: 700;
    color: var(--gold);
    font-size: 50px;
    line-height: 1;
  }
  .quote-open { left: 143px; top: 140px; }
  .quote-text {
    left: 0; top: 184px; width: 467px;
    margin: 0;
    text-align: center;
    font-family: "Josefin Sans", sans-serif;
    font-weight: 600;
    font-size: 20px;
    line-height: 28.5px;
    color: var(--gold);
    text-transform: uppercase;
  }
  .quote-close { position: relative; top: 14px; margin-left: 4px; font-size: 50px; line-height: 0; }
  .quote-author {
    left: 0; top: 398px; width: 467px;
    margin: 0;
    text-align: center;
    font-family: "Josefin Sans", sans-serif;
    font-weight: 600;
    font-size: 13px;
    letter-spacing: 1px;
    color: var(--gold);
    text-transform: uppercase;
  }
</style>
</head>
<body>
  <main class="poster">
    <svg class="facets" viewBox="0 0 467 660" aria-hidden="true">
      <defs>
        <linearGradient id="facetSheen" x1="0" y1="1" x2="1" y2="0">
          <stop offset="0" stop-color="var(--facet-dark)"/>
          <stop offset="0.5" stop-color="var(--facet-light)"/>
          <stop offset="1" stop-color="var(--facet-mid)"/>
        </linearGradient>
        <linearGradient id="facetSheenLow" x1="1" y1="0" x2="0" y2="1">
          <stop offset="0" stop-color="var(--facet-dark)"/>
          <stop offset="0.5" stop-color="var(--facet-light)"/>
          <stop offset="1" stop-color="var(--facet-mid)"/>
        </linearGradient>
      </defs>
      <polygon points="0,0 134,0 134,8 0,131" fill="url(#facetSheen)"/>
      <polygon points="0,0 60,60 0,131" fill="var(--facet-dark)" opacity="0.7"/>
      <polygon points="134,0 134,131 0,131" fill="var(--facet-mid)" opacity="0.35"/>
      <polygon points="467,660 333,660 333,652 467,529" fill="url(#facetSheenLow)"/>
      <polygon points="467,660 407,600 467,529" fill="var(--facet-dark)" opacity="0.7"/>
      <polygon points="333,529 467,529 333,660" fill="var(--facet-mid)" opacity="0.35"/>
    </svg>
    <div class="instrument-panel" role="img" aria-label="Photo of aircraft cockpit instruments"></div>
    <div class="back-frame"></div>
    <div class="quote-panel"></div>
    <div class="building-photo" role="img" aria-label="Photo of the red-brick property the business purchased"></div>
    <div class="aircraft-drawing aircraft-top" role="img" aria-label="Line drawing of a light aircraft, side view"></div>
    <div class="aircraft-drawing aircraft-left" role="img" aria-label="Line drawing of a light aircraft, front view"></div>
    <div class="aircraft-drawing aircraft-bottom" role="img" aria-label="Line drawing of a light aircraft, top view"></div>
    <span class="quote-mark quote-open">“</span>
    <p class="quote-text">It is not because<br>things are difficult<br>that we do not<br>dare; it is because<br>we do not dare<br>that they are<br>difficult.<span class="quote-mark quote-close">”</span></p>
    <p class="quote-author">Talvio</p>
  </main>
</body>
</html>
```